Re-launching marine insurance adjusting company - looking for energy

I am a sole practitioner specializing in the profession of average adjusting. There is an on-line brochure at www.kbrtmarine.example I am one of only a handful of specialists in this field and I enjoy a fair amount of name recognition, domestically in the US and internationally. My principal markets are the US, the London and Scandinavian insurance markets and shipowners and insurers in Latin America.
The business is a mixture of law, accounting and insurance and my clientele relies on a time-sensitive and accurate work-product, clearly stating an insurance company's liability for a given claim. The identity needs to project gravitas rather than flash.
Since 1998 I have traded as "The Halloway Bureau" but have also attempted to establish the name KBRTMARINE.example so that people would visit my website.
I want to implement a single identity across my stationery, business cards and website. I have come to see "The Halloway Bureau" as rather fatuous, since there is no company, it is just me. The Internet domain KBRTMARINE is long-established and I would be reluctant to change it. I have considered trading as simply Marcus T Holloway, MTH, KBRTMARINE or attempting to come up with a name that could be abbreviated to MTH, e.g. M Holloway Tessellate - but I can't find a suitable word for the second S.
Logo-wise, I have considered a stylized MTH or KBRTMARINE redolent of waves of the sea. A nautical theme embodying a cargo ship, navigational beacon or lighthouse might be appropriate but these tend to be hackneyed.
I have attached a card that I mocked up at Zib, connoting stacking up numbers, which I really like, but I think it is too cryptic for people in most insurance companies, who don't particularly think laterally or they wouldn't work in marine insurance, and the card that I use currently, which I intended to be understated, but in fact it states nothing.
I have also attached my current letterhead, to demonstrate how I really need help.
Finally, I have attached a credentials sheet, to attempt to establish how narrow and deep is the professional niche that I occupy.
What I am looking to implement is a single logo, font, them and color scheme to use across my website, letterhead and business cards.
Over to the Pencil Guild...
Ship owners and insurance companies
Accounting

```html
<!DOCTYPE html>
<html lang="en">
<head>
<meta charset="utf-8">
<title>KBRTMARINE Letterhead</title>
<link rel="stylesheet" href="https://fonts.googleapis.com/css2?family=Montserrat:wght@400;600&display=swap">
<style>
  :root {
    --backdrop: #939397;
    --paper: #ffffff;
    --navy: #283679;
    --sky: #30a2dc;
    --rule: #ffffff;
    --ink-light: #ffffff;
  }
  * { margin: 0; padding: 0; box-sizing: border-box; }
  html, body {
    width: 1200px;
    height: 1000px;
    overflow: hidden;
    background: var(--backdrop);
  }
  .canvas {
    position: relative;
    width: 1200px;
    height: 1000px;
    display: flex;
    align-items: center;
    justify-content: center;
  }
  .letterhead {
    position: relative;
    width: 712px;
    height: 920px;
    background: var(--paper);
    box-shadow: 0 4px 14px rgba(0, 0, 0, 0.25);
    overflow: hidden;
  }
  .letterhead__brand {
    position: absolute;
    top: 74px;
    left: 0;
    width: 100%;
    padding-left: 70px;
    text-align: center;
  }
  .brand-name {
    font-family: "Montserrat", sans-serif;
    font-weight: 600;
    font-size: 26px;
    letter-spacing: 2px;
    color: var(--navy);
  }
  .letterhead__footer-art {
    position: absolute;
    left: 0;
    bottom: 0;
    width: 712px;
    height: 920px;
  }
  .wave--navy { fill: var(--navy); }
  .wave--sky { fill: var(--sky); }
  .wave--rule { fill: none; stroke: var(--rule); stroke-width: 2; }
  .contact-row {
    position: absolute;
    left: 30px;
    right: 24px;
    bottom: 22px;
    display: flex;
    justify-content: space-between;
    align-items: center;
    list-style: none;
    font-family: "Montserrat", sans-serif;
    font-weight: 400;
    font-size: 9.5px;
    color: var(--ink-light);
  }
  .contact-row__item {
    display: flex;
    align-items: center;
    gap: 5px;
    white-space: nowrap;
  }
  .contact-icon {
    width: 9px;
    height: 9px;
    fill: var(--ink-light);
  }
</style>
</head>
<body>
<main class="canvas">
  <article class="letterhead">
    <header class="letterhead__brand">
      <span class="brand-name">KBRTMARINE</span>
    </header>

    <svg class="letterhead__footer-art" viewBox="0 0 712 920" aria-hidden="true">
      <path class="wave--navy" d="M0,730 C200,712 380,782 480,836 C565,880 662,868 712,790 L712,920 L0,920 Z"/>
      <path class="wave--sky" d="M0,756 C200,742 380,806 480,858 C565,900 662,890 712,818 L712,920 L0,920 Z"/>
      <path class="wave--rule" d="M0,752 C200,738 380,802 480,854 C565,896 662,886 712,814"/>
    </svg>

    <ul class="contact-row">
      <li class="contact-row__item">
        <svg class="contact-icon" viewBox="0 0 10 10"><path d="M2,0 L4,0 L4.5,2.5 L3.2,3.4 C3.8,4.9 5.1,6.2 6.6,6.8 L7.5,5.5 L10,6 L10,8 C10,9 9,10 8,10 C3.6,10 0,6.4 0,2 C0,1 1,0 2,0 Z"/></svg>
        (212) 555 0148
      </li>
      <li class="contact-row__item">
        <svg class="contact-icon" viewBox="0 0 10 10"><path d="M2.5,0 H7.5 A1,1 0 0 1 8.5,1 V9 A1,1 0 0 1 7.5,10 H2.5 A1,1 0 0 1 1.5,9 V1 A1,1 0 0 1 2.5,0 Z M3,1.5 V7.5 H7 V1.5 Z"/></svg>
        (212) 555 0172
      </li>
      <li class="contact-row__item">
        <svg class="contact-icon" viewBox="0 0 10 10"><path d="M0,2 H10 V8 H0 Z M0.6,2.4 L5,5.6 L9.4,2.4" stroke="#30a2dc" stroke-width="0.8"/></svg>
        info@kbrtmarine.example
      </li>
      <li class="contact-row__item">
        <svg class="contact-icon" viewBox="0 0 10 10"><circle cx="5" cy="5" r="4.3" fill="none" stroke="#fff" stroke-width="1.2"/><path d="M0.7,5 H9.3 M5,0.7 C2.8,3 2.8,7 5,9.3 M5,0.7 C7.2,3 7.2,7 5,9.3" fill="none" stroke="#fff" stroke-width="0.8"/></svg>
        www.kbrtmarine.example
      </li>
      <li class="contact-row__item">
        <svg class="contact-icon" viewBox="0 0 10 10"><path d="M5,0 A3.6,3.6 0 0 1 8.6,3.6 C8.6,6 5,10 5,10 C5,10 1.4,6 1.4,3.6 A3.6,3.6 0 0 1 5,0 Z"/><circle cx="5" cy="3.6" r="1.3" fill="#30a2dc"/></svg>
        48 Harbor View Lane, New York, NY 10099, USA
      </li>
    </ul>
  </article>
</main>
</body>
</html>
```